We are a company with over 35 years experience supporting our customers IT needs. Implementing wa..*

We want customers to see a strong product line that is covered by our sales and service team.

We sell and service Impact, Mobile and thermal printers. We sell and support fiber optics, data cabling and wireless communications. We manufacture rack labels for warehouse distribution centers and also make shipping labels and private custom labels and all barcode scanning equipment used for receiving, picking and inventory control. We have custom software solutions for WMS and DIstribution Centers.

We support customers like Brenvale, Fizzo Rita, Grillmont Hut, Kavesa, Supermarket chains and 3PL companies.

Looking for a modern design to attract customer who purchase brands we distribute and support. Products from Labelworx, QDV, Quillam Mobile, MERU, Veridash Scanners, Halvor Networking Equipment to name a few.

Target Market(s)

3PL, Distribution, Bottling Companies, Supermarket Chains, Pharmaceutical

Colors

Designer to choose colors to be used in the design.

Requirements
Must have
• Warehouse Environment or Distribution Center feel.
Nice to have
• Brands we support
Should not have
• Online store feel

```html
<!DOCTYPE html>
<html lang="en">
<head>
<meta charset="utf-8">
<title>Corvane Group</title>
<link href="https://fonts.googleapis.com/css2?family=Nunito:wght@400;600;700;800;900&family=Nunito+Sans:wght@400;600;700&display=swap" rel="stylesheet">
<style>
:root{
  --orange:#e8561f;
  --orange-soft:#f07a2a;
  --green:#2f6535;
  --green-deep:#24522a;
  --ink:#1f1f1f;
  --text:#555;
  --grey-bg:#f1f1f1;
  --card-bg:#f7f7f7;
  --footer:#1d1d1d;
  --white:#fff;
}
*{box-sizing:border-box;margin:0;padding:0}
html,body{width:1200px;height:4454px;overflow:hidden}
body{font-family:"Nunito Sans",sans-serif;color:var(--text);background:var(--white);position:relative}
.abs{position:absolute}
.heading{font-family:"Nunito",sans-serif;font-weight:900;color:var(--ink)}
.btn{position:absolute;display:flex;align-items:center;justify-content:center;gap:8px;background:var(--orange);color:#fff;font-family:"Nunito",sans-serif;font-weight:800;font-size:15px;border-radius:22px;box-shadow:0 4px 10px rgba(232,86,31,.3);text-transform:uppercase;letter-spacing:.2px}
.bar{position:absolute;height:4px;width:74px;background:var(--green)}
.bar.white{background:#fff}

/* header */
.site-header{position:absolute;top:0;left:0;width:1200px;height:111px;background:#fff}
.brand{position:absolute;left:143px;top:34px;display:flex;align-items:center;gap:10px;font-family:"Nunito",sans-serif;font-weight:900;font-size:30px;color:var(--green)}
.brand i{width:16px;height:16px;border-radius:50%;background:var(--orange);display:block}
.contact-strip{position:absolute;top:18px;left:568px;display:flex;gap:28px;font-weight:700;font-size:18px;color:var(--ink)}
.contact-strip span{display:flex;align-items:center;gap:10px}
.ic{width:32px;height:32px;border-radius:50%;background:var(--orange);display:flex;align-items:center;justify-content:center}
.nav{position:absolute;top:72px;left:428px;display:flex;gap:25px;font-family:"Nunito",sans-serif;font-weight:800;font-size:15px;color:var(--ink)}
.nav .active{color:var(--orange)}

/* hero */
.hero{position:absolute;top:111px;left:0;width:1200px;height:650px;overflow:hidden}
.hero-photo{position:absolute;inset:0;background:linear-gradient(100deg,#c8642a 0%,#8a6a3c 35%,#4f7a45 60%,#5f8a52 100%)}
.hero h1{position:absolute;left:143px;top:205px;font-family:"Nunito",sans-serif;font-weight:900;font-size:52px;color:#fff}
.hero p{position:absolute;left:145px;top:280px;width:440px;font-weight:700;font-size:19px;line-height:29px;color:#fff}
.dots{position:absolute;left:147px;top:459px;display:flex;gap:12px;align-items:center}
.dots i{width:12px;height:12px;border-radius:50%;background:#fff;display:block}
.dots i.on{width:24px;height:24px;border:2px solid #fff;background:transparent;position:relative}
.dots i.on:after{content:"";position:absolute;inset:4px;border-radius:50%;background:#fff}

/* welcome */
.welcome-frame{position:absolute;left:164px;top:859px;width:362px;height:358px;border:3px solid var(--green)}
.welcome-photo{position:absolute;left:149px;top:877px;width:361px;height:357px;background:linear-gradient(135deg,#7a6048,#c9a16a 50%,#b8c84a)}
.eyebrow{position:absolute;left:569px;top:870px;font-family:"Nunito",sans-serif;font-weight:600;font-size:23px;color:var(--orange)}
.welcome h2{position:absolute;left:569px;top:905px;font-size:38px}
.welcome p{position:absolute;left:569px;top:996px;width:480px;font-size:14.5px;line-height:25.8px}

/* services */
.services{position:absolute;top:1340px;left:0;width:1200px;height:679px;background:linear-gradient(90deg,#f0f0f0,#e7e8e9 60%,#eeeff0)}
.services h2{position:absolute;left:143px;top:126px;font-size:38px;line-height:43px}
.services .intro{position:absolute;left:143px;top:264px;width:284px;font-size:14px;line-height:23.3px;color:#333}
.svc{position:absolute;width:286px;height:202px;background:var(--card-bg);box-shadow:0 2px 8px rgba(0,0,0,.1)}
.svc .badge{position:absolute;left:24px;top:26px;width:64px;height:64px;border-radius:50%;background:var(--orange);display:flex;align-items:center;justify-content:center}
.svc h3{position:absolute;left:110px;top:32px;font-family:"Nunito",sans-serif;font-weight:700;font-size:19px;line-height:26px;color:var(--ink)}
.svc p{position:absolute;left:24px;top:110px;width:240px;font-size:13.5px;line-height:23.5px;color:#666}

/* products */
.products{position:absolute;top:2019px;left:0;width:1200px;height:805px;background:radial-gradient(circle at 80% 20%,#3a7441,var(--green) 55%,var(--green-deep))}
.sec-title{position:absolute;left:0;width:1200px;text-align:center;font-size:38px}
.products .sec-title{color:#fff}
.prod{position:absolute;top:237px;width:284px;height:353px;background:var(--card-bg)}
.prod .shot{position:absolute;left:0;top:0;width:284px;height:203px;background:#fff;display:flex;align-items:center;justify-content:center}
.prod .shot div{width:140px;height:140px;border-radius:8px;background:linear-gradient(160deg,#3a3a3a,#111)}
.prod h3{position:absolute;top:232px;width:284px;text-align:center;font-family:"Nunito",sans-serif;font-weight:700;font-size:18.5px;color:var(--ink)}
.prod p{position:absolute;top:268px;left:22px;width:240px;text-align:center;font-size:13.5px;line-height:21px;color:#666}

/* blog */
.post{position:absolute;top:3033px;width:287px;height:384px;background:#fff;border:1px solid #ddd;border-radius:6px;overflow:hidden}
.post .thumb{height:183px}
.post h3{position:absolute;left:17px;top:212px;width:250px;font-family:"Nunito",sans-serif;font-weight:700;font-size:15.5px;line-height:22px;color:var(--ink)}
.post .date{position:absolute;left:17px;top:266px;display:flex;align-items:center;gap:10px;font-weight:700;font-size:14px;color:var(--orange)}
.post .date i{width:20px;height:20px;border-radius:50%;background:var(--orange);display:block}
.post p{position:absolute;left:17px;top:306px;width:256px;font-size:13.5px;line-height:22px;color:#555}

/* customers */
.customers{position:absolute;top:3545px;left:0;width:1200px;height:500px;background:var(--grey-bg)}
.client{position:absolute;top:195px;width:176px;height:78px;background:#fff;border:1px solid #ddd;display:flex;align-items:center;justify-content:center;font-family:"Nunito",sans-serif;font-weight:800;font-size:20px;color:var(--ink)}
.arrow{position:absolute;top:218px;width:30px;height:34px}

/* footer */
.footer{position:absolute;top:3933px;left:0;width:1200px;height:521px}
.footer h4{position:absolute;top:109px;font-family:"Nunito",sans-serif;font-weight:800;font-size:18px;color:#fff}
.footer .col{position:absolute;top:158px;color:#ddd;font-size:14px;line-height:20px}
.contact-item{display:flex;gap:14px;margin-bottom:18px}
.links li{list-style:none;margin-bottom:7.3px}
.field{position:absolute;height:40px;border:1px solid #bbb;color:#eee;font-size:12px;padding:13px 12px}
.submit{position:absolute;left:667px;top:303px;width:211px;height:38px;background:var(--orange);color:#fff;font-weight:800;font-size:15px;display:flex;align-items:center;justify-content:center}
.legal{position:absolute;left:0;top:421px;width:1200px;border-top:1px solid #333;text-align:center;padding-top:36px;font-size:13px;color:#ddd}
</style>
</head>
<body>

<header class="site-header">
  <div class="brand"><i></i>Corvane Group</div>
  <div class="contact-strip">
    <span><span class="ic"><svg width="16" height="16" viewBox="0 0 24 24"><path fill="#fff" d="M6.6 10.8a15 15 0 0 0 6.6 6.6l2.2-2.2c.3-.3.7-.4 1-.2 1.1.4 2.3.6 3.6.6.6 0 1 .4 1 1V20c0 .6-.4 1-1 1A17 17 0 0 1 3 4c0-.6.4-1 1-1h3.5c.6 0 1 .4 1 1 0 1.3.2 2.5.6 3.6.1.3 0 .7-.2 1z"/></svg></span>1-800-555-0142</span>
    <span><span class="ic"><svg width="16" height="16" viewBox="0 0 24 24"><rect x="3" y="5" width="18" height="14" rx="2" fill="#fff"/><path d="M3 6l9 7 9-7" stroke="#e8561f" stroke-width="2" fill="none"/></svg></span>hello@corvanegroup.example</span>
  </div>
  <nav class="nav"><span class="active">HOME</span><span>ABOUT US</span><span>OUR PRODUCTS</span><span>OUR CUSTOMERS</span><span>NEWS</span><span>CONTACT</span></nav>
</header>

<section class="hero">
  <div class="hero-photo" role="img" aria-label="Close-up of network patch cables plugged into a switch, with orange and green tint"></div>
  <svg class="abs" style="left:0;top:0" width="1200" height="650" viewBox="0 0 1200 650">
    <path d="M0 600 C 200 660 380 650 600 600 C 850 545 1050 470 1200 370 L1200 650 L0 650 Z" fill="#fff"/>
    <path d="M560 645 C 800 615 1050 520 1200 448" stroke="#e8561f" stroke-width="8" fill="none"/>
  </svg>
  <h1>Corvane Group</h1>
  <p>Sed ut perspiciatis unde omnis iste natus error sit voluptatem accusantium doloremque laudantium, totam rem aperiam, eaque ipsa</p>
  <div class="btn" style="left:145px;top:408px;width:213px;height:41px">FIND OUT MORE <svg width="14" height="14" viewBox="0 0 14 14"><path d="M1 7h11M8 3l4 4-4 4" stroke="#fff" stroke-width="2" fill="none"/></svg></div>
  <div class="dots"><i class="on"></i><i></i><i></i><i></i></div>
</section>

<section class="welcome">
  <div class="welcome-frame"></div>
  <div class="welcome-photo" role="img" aria-label="Warehouse worker in a high-visibility vest scanning stock between racks"></div>
  <div class="eyebrow">WELCOME TO</div>
  <h2 class="heading">Corvane Group</h2>
  <p>Sed ut perspiciatis unde omnis iste natus error sit voluptatem accuntium doloremque laudantium, totam rem aperiam, eaque ipsa quae ab illo inore veritatis et quasi architecto beatae vitae dicta sunt explicabo. Nemo enim ipsam voluptatem quia voluptas sit aspernatur aut odit aut fugit, sed quia consequuntur magni dolores eos qui ratione voluptatem sequi nesciunt. Neque porro quisquam est, qui dolorem ipsum quia dolor</p>
  <div class="btn" style="left:569px;top:1175px;width:174px;height:41px">LEARN MORE <svg width="14" height="14" viewBox="0 0 14 14"><path d="M1 7h11M8 3l4 4-4 4" stroke="#fff" stroke-width="2" fill="none"/></svg></div>
</section>

<section class="services">
  <h2 class="heading">OUR<br>SERVICES</h2>
  <div class="bar" style="left:143px;top:235px"></div>
  <p class="intro">Sed ut perspiciatis unde omnis iste natus error sit voluptatem accusantium doloremque laudantium, totam rem aperiam, eaque ipsa quae ab illo inventore veritatis et quasi architecto beatae vitae dicta sunt explicabo. Nemo enim ipsam voluptatem quia voluptas sit aspernatur aut odit aut fugit, sed quia</p>
  <div class="btn" style="left:143px;top:473px;width:175px;height:41px">LEARN MORE <svg width="14" height="14" viewBox="0 0 14 14"><path d="M1 7h11M8 3l4 4-4 4" stroke="#fff" stroke-width="2" fill="none"/></svg></div>

  <div class="svc" style="left:462px;top:109px"><div class="badge"><svg width="34" height="34" viewBox="0 0 34 34" fill="none" stroke="#fff" stroke-width="2"><rect x="5" y="16" width="24" height="12" rx="2"/><path d="M9 16V6M14 16V6M20 16V6M25 16V6"/></svg></div><h3>Support<br>Fiber Optics</h3><p>Sed ut perspiciatis unde omnis iste natus sit voluptatem accusantium doloremque laium, totam</p></div>
  <div class="svc" style="left:769px;top:109px"><div class="badge"><svg width="34" height="34" viewBox="0 0 34 34" fill="none" stroke="#fff" stroke-width="2"><circle cx="15" cy="19" r="11"/><circle cx="15" cy="19" r="6"/><path d="M22 10l6-6"/></svg></div><h3>Data<br>Cabling</h3><p>Sed ut perspiciatis unde omnis iste natus sit voluptatem accusantium doloremque laium, totam</p></div>
  <div class="svc" style="left:462px;top:332px"><div class="badge"><svg width="34" height="34" viewBox="0 0 34 34" fill="none" stroke="#fff" stroke-width="2"><rect x="6" y="6" width="22" height="22" rx="3"/><path d="M11 22a6 6 0 0 1 12 0M14 22a3 3 0 0 1 6 0"/></svg></div><h3>Wireless<br>Communications</h3><p>Sed ut perspiciatis unde omnis iste natus sit voluptatem accusantium doloremque laium, totam</p></div>
  <div class="svc" style="left:769px;top:332px"><div class="badge"><svg width="34" height="34" viewBox="0 0 34 34" fill="none" stroke="#fff" stroke-width="2"><circle cx="17" cy="17" r="6"/><path d="M17 4v5M17 25v5M4 17h5M25 17h5M8 8l3 3M23 23l3 3M26 8l-3 3M8 26l3-3"/></svg></div><h3>Custom Software<br>Solutions</h3><p>Sed ut perspiciatis unde omnis iste natus sit voluptatem accusantium doloremque laium, totam</p></div>
</section>

<section class="products">
  <h2 class="heading sec-title" style="top:96px">OUR PRODUCTS</h2>
  <div class="bar white" style="left:563px;top:161px"></div>
  <div class="prod" style="left:145px"><div class="shot"><div role="img" aria-label="Enclosed pedestal line matrix printer"></div></div><h3>L8000 Enclosed Pedestal</h3><p>Sed ut perspiciatis unde omnis iste natus sit voluptatem accusantium doloremque laudantium</p></div>
  <div class="prod" style="left:458px"><div class="shot"><div role="img" aria-label="Industrial barcode label printer"></div></div><h3>Industrial Barcode Printers</h3><p>Sed ut perspiciatis unde omnis iste natus sit voluptatem accusantium doloremque laudantium</p></div>
  <div class="prod" style="left:771px"><div class="shot"><div role="img" aria-label="Handheld mobile receipt printer"></div></div><h3>Mobile Portable Printers</h3><p>Sed ut perspiciatis unde omnis iste natus sit voluptatem accusantium doloremque laudantium</p></div>
  <div class="btn" style="left:470px;top:658px;width:258px;height:41px">VIEW MORE PRODUCTS <svg width="14" height="14" viewBox="0 0 14 14"><path d="M1 7h11M8 3l4 4-4 4" stroke="#fff" stroke-width="2" fill="none"/></svg></div>
</section>

<section class="blog">
  <h2 class="heading sec-title" style="top:2910px">LATEST BLOG</h2>
  <div class="bar" style="left:563px;top:2975px"></div>
  <article class="post" style="left:143px"><div class="thumb" role="img" aria-label="Team checking parcels in a distribution warehouse" style="background:linear-gradient(135deg,#6d5a48,#b89270)"></div><h3>Nemo Enim Ipsam Voluptatem Quia Voluptas Sit</h3><div class="date"><i></i>JAN 15,2020</div><p>Sed ut perspiciatis unde omnis iste natus error sit voluptatem accusantium doloque laium, totam rem aperiam</p></article>
  <article class="post" style="left:455px"><div class="thumb" role="img" aria-label="City at dusk with glowing network connection lines" style="background:linear-gradient(180deg,#2a4a78,#5a6a8a 50%,#c98a3a)"></div><h3>Nemo Enim Ipsam Voluptatem Quia Voluptas Sit</h3><div class="date"><i></i>JAN 15,2020</div><p>Sed ut perspiciatis unde omnis iste natus error sit voluptatem accusantium doloque laium, totam rem aperiam</p></article>
  <article class="post" style="left:768px"><div class="thumb" role="img" aria-label="Hands typing code at a computer workstation" style="background:linear-gradient(135deg,#d8dde2,#4a5460 60%,#1e242c)"></div><h3>Nemo Enim Ipsam Voluptatem Quia Voluptas Sit</h3><div class="date"><i></i>JAN 15,2020</div><p>Sed ut perspiciatis unde omnis iste natus error sit voluptatem accusantium doloque laium, totam rem aperiam</p></article>
</section>

<section class="customers">
  <h2 class="heading sec-title" style="top:85px">OUR CUSTOMERS</h2>
  <div class="bar" style="left:572px;top:150px;width:56px"></div>
  <svg class="arrow" style="left:84px" viewBox="0 0 30 34"><path d="M20 3L7 17l13 14" stroke="#bbb" stroke-width="2" fill="none"/></svg>
  <div class="client" style="left:133px">Brenvale</div>
  <div class="client" style="left:323px">Fizzo Rita</div>
  <div class="client" style="left:514px">Grillmont Hut</div>
  <div class="client" style="left:704px">Kavesa</div>
  <div class="client" style="left:894px">Stackline Hub</div>
  <svg class="arrow" style="left:1086px" viewBox="0 0 30 34"><path d="M10 3l13 14-13 14" stroke="#bbb" stroke-width="2" fill="none"/></svg>
</section>

<footer class="footer">
  <svg class="abs" style="left:0;top:0" width="1200" height="521" viewBox="0 0 1200 521">
    <path d="M0 60 C 300 20 600 -5 850 5 C 1000 12 1120 40 1200 95 L1200 521 L0 521 Z" fill="#1d1d1d"/>
    <path d="M1030 20 C 1110 40 1170 75 1200 110 L1200 150 C 1170 100 1110 55 1030 20 Z" fill="#e8561f"/>
  </svg>
  <h4 style="left:147px">CONTACT US</h4>
  <h4 style="left:463px">QUICK LINKS</h4>
  <h4 style="left:667px">REQUEST A QUOTE</h4>
  <div class="col" style="left:147px;width:240px">
    <div class="contact-item"><svg width="16" height="18" viewBox="0 0 16 18"><path d="M8 1a6 6 0 0 1 6 6c0 4-6 10-6 10S2 11 2 7a6 6 0 0 1 6-6z" stroke="#ddd" fill="none" stroke-width="1.5"/><circle cx="8" cy="7" r="2" fill="#ddd"/></svg><span>Corvane Group<br>48 Millrace Way, Dunmore,<br>NV, 89000</span></div>
    <div class="contact-item"><svg width="16" height="16" viewBox="0 0 24 24"><path stroke="#ddd" stroke-width="1.5" fill="none" d="M6.6 10.8a15 15 0 0 0 6.6 6.6l2.2-2.2c.3-.3.7-.4 1-.2 1.1.4 2.3.6 3.6.6.6 0 1 .4 1 1V20c0 .6-.4 1-1 1A17 17 0 0 1 3 4c0-.6.4-1 1-1h3.5c.6 0 1 .4 1 1 0 1.3.2 2.5.6 3.6.1.3 0 .7-.2 1z"/></svg><span>Phone:<br>808-555-0187</span></div>
    <div class="contact-item"><svg width="16" height="14" viewBox="0 0 16 14"><rect x="1" y="1" width="14" height="12" stroke="#ddd" fill="none" stroke-width="1.5"/><path d="M1 2l7 6 7-6" stroke="#ddd" fill="none" stroke-width="1.5"/></svg><span>Email:<br>hello@corvanegroup.example</span></div>
  </div>
  <ul class="col links" style="left:463px"><li>Home</li><li>About Us</li><li>Services</li><li>Products</li><li>News And Events</li><li>Shop</li><li>Contact</li></ul>
  <div class="col" style="left:667px;font-size:13px">Alternatively You Can Fill In The Following Contact Form:</div>
  <div class="field" style="left:667px;top:194px;width:187px">Name</div>
  <div class="field" style="left:865px;top:194px;width:186px">E - Mail</div>
  <div class="field" style="left:667px;top:243px;width:187px">Subject</div>
  <div class="field" style="left:865px;top:243px;width:186px">Message</div>
  <div class="submit">SUBMIT</div>
  <div class="legal">(c) 2020 Corvane Group | All Rights Reserved | Disclaimer</div>
</footer>

</body>
</html>
```